VARLEN Consulting Services “Coming Soon” Landing Page

MORE INTO IN Design Brief for Web Designer document attached

1. Project Overview
Client: VARLEN Consulting Services
Project: Build a static, responsive “Coming Soon” landing page (HTML/CSS/JS)
Timeline: Target launch date in June 7, 2025
Point of Contact: Martin Hallowby (Managing Director)
 • Email: mart@varlenconsulting.example
 • Phone: 415-738-2094
Background:
VARLEN Consulting Services is a boutique IT consultancy specializing in enterprise cloud solutions, microservices, FlowMesh migrations, and AGENTIC AI-driven integrations. We are launching a new website to capture CIO-level leads, build brand awareness, and communicate our key value propositions before the full site goes live. This “Coming Soon” page should reflect our brand identity, target CIO and enterprise IT leaders, and collect email addresses for early access to whitepapers, case studies, and consultations.

2. Goals & Objectives
1. Brand Reinforcement
• Convey a contemporary, corporate, and professional look that aligns with VARLEN’s positioning as a specialized, agile, high-ROI consultancy.
• Utilize our brand colors (green, red, blue, gold) and typography (Segoe UI) consistently.
2. Lead Generation
• Implement a simple email-capture form (“Notify Me”) that submits to mailto:info@varlenconsulting.example.
• Convey clear messaging so visitors understand why they should sign up (exclusive early insights, whitepapers, invitations to consult).
3. Enterprise Leadership-Focused Messaging
• Immediately communicate our core value proposition (“Enterprise Modernization Reimagined”) and differentiation versus larger consulting firms.
• Introduce AGENTIC AI use cases to demonstrate cutting-edge capabilities.
4. Responsive & Accessible
• Build a mobile-first responsive design using a 12-column grid.
• Follow best practices for HTML5 markup, CSS3, and lightweight JS (for countdown timer).
5. SEO & Technical Must-Haves
• Include basic SEO metadata and Open Graph tags.
• Provide a favicon placeholder.
• Placeholder for a Privacy Policy link in the footer.

Designs look the same

VARLEN Consulting Services is a boutique IT consultancy specializing in enterprise cloud solutions, microservices, FlowMesh migrations, and AGENTIC AI-driven integrations.

• Below are our primary brand colors with hex codes (derived from CMYK values in the uploaded “Color and Font.jpg”): • Green (Globe Icon): #3BFF05 • Red (Q-Shape Icon): #EF1C03 • Blue (Circle Icon): #456EFF • Gold (Connector Icon): #F7C217 • Dark Gray / Text Color: #1A1A1A Use these colors for text highlights, buttons, icons, and accents. The overall page background is white or very light gray (#F9F9F9) to keep the design clean.
• Colors outside the scheme provided

```html
<!DOCTYPE html>
<html lang="en">
<head>
<meta charset="utf-8">
<title>VARLEN Consulting Services – Coming Soon</title>
<link rel="stylesheet" href="https://fonts.googleapis.com/css2?family=Open+Sans:wght@400;600;700&family=Noto+Sans:wght@600;700&display=swap">
<style>
:root{
  --blue:#456EFF;
  --navy:#0B2A5B;
  --deep:#00214A;
  --gold:#F7C217;
  --green:#0DBB3C;
  --red:#EF3A2E;
  --text:#1A1A1A;
  --light:#EEF2F8;
  --card:#F7F6F8;
  --white:#FFFFFF;
}
*{box-sizing:border-box;margin:0;padding:0}
html,body{width:1200px;height:4338px;overflow:hidden}
body{font-family:"Open Sans",sans-serif;color:var(--text);background:var(--white);position:relative}
.abs{position:absolute}
.btn{position:absolute;display:flex;align-items:center;justify-content:center;border-radius:6px;font-size:21px;font-weight:400;color:var(--text)}
.btn-blue{background:var(--blue);color:var(--white)}
.btn-gold{background:var(--gold)}
.btn-green{background:var(--green);color:var(--white)}
.heading{font-family:"Noto Sans",sans-serif;font-weight:700;color:var(--navy);letter-spacing:2px}

.topbar{left:0;top:0;width:1200px;height:40px;background:var(--blue);color:var(--white);font-size:14px}
.topbar .phone{left:88px;top:11px;display:flex;align-items:center;gap:6px}
.topbar .social{right:88px;top:12px;display:flex;gap:6px}
.topbar .social span{width:16px;height:16px;border:2px solid var(--white);border-radius:3px}

.nav{left:0;top:40px;width:1200px;height:95px;background:var(--white)}
.brand{left:88px;top:24px;display:flex;align-items:center;gap:12px}
.brand .dot{width:40px;height:40px;border-radius:50%;background:var(--blue)}
.brand .name{font-size:28px;font-weight:600;color:var(--text);letter-spacing:.5px}
.menu{right:88px;top:38px;display:flex;gap:40px;font-size:18px;font-weight:600}
.menu .active{border-bottom:2px solid var(--red);padding-bottom:4px}

.hero{left:0;top:135px;width:1200px;height:538px;background:#000}
.hero-art{left:626px;top:15px;width:574px;height:508px;background:radial-gradient(ellipse at 55% 40%,#3FA7FF 0%,#1646C8 35%,#06145A 70%,#000 100%)}
.hero h1{left:88px;top:50px;font-family:"Noto Sans",sans-serif;font-size:51px;line-height:66px;color:var(--white);letter-spacing:2px;font-weight:700}
.hero p{left:88px;top:262px;width:560px;font-size:22px;line-height:31px;color:var(--white)}

.about h2{font-size:33px}
.about-text{left:104px;top:840px;width:640px;font-size:19px;line-height:37.5px}
.about-photo{left:798px;top:761px;width:333px;height:459px;background:linear-gradient(160deg,#1C3F8F,#0B1B3A 60%,#2A2E3A)}

.cluster .c{position:absolute;border-radius:50%;background:var(--white);box-shadow:0 4px 14px rgba(0,0,0,.14)}
.cluster .p{background:linear-gradient(#8A7A70,#4A4A52)}
.diff h2{font-size:34px;letter-spacing:1px}
.diff ul{list-style:none;left:540px;top:1426px;width:590px;font-size:19px;line-height:37.5px}
.diff li{padding-left:24px;position:relative}
.diff li::before{content:"";position:absolute;left:0;top:12px;width:15px;height:15px;border-radius:50%;background:var(--green)}
.diff li::after{content:"";position:absolute;left:4px;top:15px;width:5px;height:8px;border:solid var(--white);border-width:0 2px 2px 0;transform:rotate(40deg)}
.hl{color:var(--blue);font-weight:600}

.briefing{left:0;top:1991px;width:1200px;height:433px;background:var(--light);text-align:center}
.center{width:1200px;left:0;text-align:center}

.countdown{left:0;top:2424px;width:1200px;height:377px;background:var(--deep);color:var(--white)}
.unit{position:absolute;width:140px;text-align:center;top:152px}
.unit b{display:block;font-family:"Noto Sans",sans-serif;font-size:92px;line-height:92px;color:var(--red);font-weight:700}
.unit span{display:block;font-size:30px;margin-top:4px}

.card{position:absolute;top:3151px;width:489px;height:535px;background:var(--card);border:1.5px solid #8A8A92;border-radius:10px}
.card h3{position:absolute;left:35px;font-family:"Noto Sans",sans-serif;font-size:28px;line-height:40px;color:var(--navy);font-weight:700}
.card ul{position:absolute;left:35px;width:420px;list-style:none;font-size:17px;line-height:37.5px}
.card li{padding-left:18px;position:relative}
.card li::before{content:"";position:absolute;left:0;top:17px;width:5px;height:5px;border-radius:50%;background:var(--blue)}

.signup{left:0;top:3842px;width:1200px;height:496px;background:var(--deep);color:var(--white)}
.email{left:313px;top:291px;width:428px;height:54px;background:var(--white);border-radius:6px 0 0 6px;color:var(--text);font-size:20px;padding:15px 0 0 45px}
</style>
</head>
<body>

<header>
  <div class="abs topbar">
    <div class="abs phone">
      <svg width="10" height="16" viewBox="0 0 10 16"><rect x="0" y="0" width="10" height="16" rx="2" fill="#fff"/></svg>
      415-738-2094
    </div>
    <div class="abs social"><span></span><span></span><span></span></div>
  </div>
  <nav class="abs nav">
    <div class="abs brand"><span class="dot"></span><span class="name">VARLEN</span></div>
    <div class="abs menu"><span class="active">HOME</span><span>SERVICES</span><span>ABOUT</span><span>CONTACT</span></div>
  </nav>
</header>

<section class="abs hero">
  <div class="abs hero-art" role="img" aria-label="Glowing digital cloud above a circuit-board city"></div>
  <h1 class="abs">Enterprise<br>Modernization<br>Reimagined</h1>
  <p class="abs">Retire legacy systems and transition to secure, cloud-native infrastructure designed for scalability, AI integration, and future -ready performance.</p>
  <div class="btn btn-blue" style="left:89px;top:392px;width:148px;height:54px">Notify Me</div>
  <div class="btn btn-gold" style="left:274px;top:392px;width:229px;height:54px">See Our Approach</div>
</section>

<section class="about">
  <h2 class="abs heading" style="left:104px;top:762px">ABOUT US</h2>
  <p class="abs about-text">Imagine a partner that doesn’t hand you a recycled playbook<br>—but builds a smarter path forward that’s all about your goals.<br>At VARLEN Consulting Services, we don’t do cookie-cutter.<br>We roll up our sleeves, work alongside your team, and deliver fast,<br>measurable results that move the needle.&nbsp; While others push<br>templates, we unlock possibilities—modern systems, real efficiency,<br>and AI that actually works. No fluff. No junior handoffs.<br>Just bold execution that gets you ahead—and keeps you there.</p>
  <div class="btn btn-green" style="left:106px;top:1180px;width:162px;height:52px;font-size:20px">Learn More</div>
  <div class="abs about-photo" role="img" aria-label="Consulting team meeting with tablets under a cloud diagram display"></div>
</section>

<section class="diff">
  <div class="abs cluster" style="left:0;top:0">
    <div class="c" style="left:141px;top:1420px;width:90px;height:90px"></div>
    <div class="c" style="left:336px;top:1420px;width:90px;height:90px"></div>
    <div class="c" style="left:96px;top:1540px;width:90px;height:90px"></div>
    <div class="c" style="left:381px;top:1540px;width:90px;height:90px"></div>
    <div class="c" style="left:237px;top:1690px;width:90px;height:90px"></div>
    <div class="c p" style="left:210px;top:1498px;width:145px;height:145px" role="img" aria-label="Lead consultant portrait"></div>
    <div class="c p" style="left:121px;top:1660px;width:98px;height:98px" role="img" aria-label="Consultant portrait"></div>
    <div class="c p" style="left:346px;top:1660px;width:98px;height:98px" role="img" aria-label="Consultant portrait"></div>
  </div>
  <h2 class="abs heading" style="left:540px;top:1350px">Why We’re Different</h2>
  <ul class="abs">
    <li><span class="hl">Senior Access, Always</span> – Speak directly to the experts.<br>No junior filters. No delays.</li>
    <li><span class="hl">Speed That Scales</span> – Rapid execution means you see value<br>faster—and scale without friction.</li>
    <li><span class="hl">Elite Expertise, Zero Fluff</span> – Our DNA is Nimbra, FlowMesh, and<br>bleeding-edge AI.</li>
    <li><span class="hl">Custom Paths to Modernization</span> – Your transformation,<br>built to fit and built to last.</li>
    <li><span class="hl">Smarter Spend</span> – High impact. Low overhead.<br>We outperform the big firms without their price tags.</li>
  </ul>
  <div class="btn btn-gold" style="left:522px;top:1835px;width:156px;height:53px;font-size:20px">Contact Us</div>
</section>

<section class="abs briefing">
  <h2 class="abs heading center" style="top:115px;font-size:33px">GET EARLY ACESS TO STRATEGIST BRIEFFINGS</h2>
  <p class="abs center" style="top:184px;font-size:21px;font-weight:600">Access exclusive briefings on AI-trend transformation.</p>
  <div class="btn btn-green" style="left:470px;top:261px;width:259px;height:54px;font-size:20px">Get the Early Briefing</div>
</section>

<section class="abs countdown">
  <h2 class="abs center" style="top:82px;font-family:'Noto Sans',sans-serif;font-size:34px;letter-spacing:3px;font-weight:600">COUNTDOWN TO LAUNCH</h2>
  <div class="unit" style="left:299px"><b>29</b><span>Days</span></div>
  <div class="unit" style="left:452px"><b>23</b><span>Hours</span></div>
  <div class="unit" style="left:608px"><b>59</b><span>Min</span></div>
  <div class="unit" style="left:761px"><b>10</b><span>Sec</span></div>
</section>

<section class="leaders">
  <h2 class="abs heading center" style="top:2905px;font-size:34px">WHY ENTERPRISE LEADERS CHOOSE VARLEN</h2>
  <p class="abs center" style="top:2966px;font-size:19px;line-height:37.5px">Today’s leaders don’t have time for templated strategies and slow-moving firms.<br>At VARLEN, we deliver tailored solutions that align with your business objectives,<br>accelerate outcomes, and scale as you grow.</p>
  <div class="card" style="left:88px">
    <h3 style="top:22px">Business Value for<br>Enterprise Leadership</h3>
    <ul style="top:142px">
      <li><span class="hl">Efficiency:</span> aligned directly with IT and business<br>strategy</li>
      <li><span class="hl">Cost-Effectiveness:</span> and improved TCO metrics</li>
      <li><span class="hl">Scalability:</span> versus traditional consulting<br>timelines</li>
      <li><span class="hl">Security &amp; Compliance:</span> no layers of junior<br>consultants</li>
    </ul>
    <div class="btn btn-gold" style="left:35px;top:447px;width:156px;height:50px;font-size:20px">Contact Us</div>
  </div>
  <div class="card" style="left:624px">
    <h3 style="top:22px">What Sets Us Apart</h3>
    <ul style="top:104px">
      <li><span class="hl">Tailored Execution</span> aligned directly with IT and<br>business strategy</li>
      <li><span class="hl">Accelerated ROI</span> and improved TCO metrics</li>
      <li><span class="hl">Faster Turnaround Times</span> versus traditional<br>consulting timelines</li>
      <li><span class="hl">Direct Access to Experts</span> no layers of junior<br>consultants</li>
      <li><span class="hl">Embedded AGENTIC AI</span> for next-gen<br>modernization intelligence</li>
    </ul>
    <div class="btn btn-gold" style="left:35px;top:447px;width:156px;height:50px;font-size:20px">Contact Us</div>
  </div>
</section>

<section class="abs signup">
  <h2 class="abs center" style="top:105px;font-family:'Noto Sans',sans-serif;font-size:33px;letter-spacing:3px;font-weight:600">BE THE FIRST TO KNOW WHEN WE GO LIVE</h2>
  <p class="abs center" style="top:180px;font-size:21px;line-height:31px">Join our list to receive early access to whitepapers,<br>case studies, and consultation opportunities.</p>
  <div class="abs email">Enter your email</div>
  <div class="btn btn-blue" style="left:741px;top:291px;width:146px;height:54px;border-radius:0 6px 6px 0;font-size:21px">Notify Me</div>
  <p class="abs center" style="top:365px;font-size:16px">We respect your time and inbox. No spam—just strategic insights.</p>
</section>

</body>
</html>
```